Skin Care business card for esthetician that is home based

I need a business card for my esthetician business. I would like to use a picture provided.
I want the picture #1 that I have provided to be as the main background with my title and the moto underneath in smaller lettering. Below that as a seperate thing I would like my full name and underneath in small letters to say "esthetician".
As a seperate paragraph I would like my address then phone number, email and my website that I have provided in the business card details.
On the back side I would like my second picture to be small and in the top left corner and then have the "nice to haves" details to be at the center bottom of the card.
Target Market(s)
mosty women between 18 and 60 years old
Industry/Entity Type
Skin Care
Contact Information for Business Card
Coastline Skin Care - Main Title
Helping you find beautiful! - motto
Lorena Bistrica Vondel -
Phone: 312.485.1937
7183 SW 9th Avenue
Dallow WA 98321
marlowskincare@examplemail.com
www.marlowskincare.example
Font styles to use
Requirements
Must have
- Picure I provided or other similar photo.
Nice to have
- On the back side:
Helping you find beautiful!
www.marlowskincare.example

```html
<!DOCTYPE html>
<html lang="en">
<head>
<meta charset="utf-8">
<title>Coastline Skin Care – Business Card</title>
<link rel="stylesheet" href="https://fonts.googleapis.com/css2?family=Crimson+Pro:ital,wght@0,400;1,700&family=Alex+Brush&display=swap">
<style>
  :root {
    --backdrop: #4a4a4a;
    --card-cream: #fdf3ec;
    --card-cream-deep: #fbe9de;
    --ink: #2b2623;
    --ink-soft: #4a423d;
    --gold: #b48a1f;
    --photo-light: #e9cbb4;
    --photo-mid: #c99a7c;
    --photo-dark: #7b5443;
  }
  * { box-sizing: border-box; margin: 0; padding: 0; }
  html, body { width: 1200px; height: 1200px; overflow: hidden; }
  body {
    background: var(--backdrop);
    font-family: "Crimson Pro", Georgia, serif;
    color: var(--ink);
    position: relative;
  }
  .card {
    position: absolute;
    left: 257px;
    width: 686px;
    height: 392px;
    border-radius: 18px;
    overflow: hidden;
    background: linear-gradient(135deg, var(--card-cream-deep), var(--card-cream) 60%, #fff8f3);
  }
  .card--front { top: 165px; }
  .card--back { top: 653px; }

  .front-photo { position: absolute; inset: 0; width: 686px; height: 392px; }

  .front-text { position: absolute; left: 24px; top: 0; width: 360px; }
  .front-text p { position: absolute; left: 0; white-space: nowrap; line-height: 1; }
  .business-name { top: 62px; font-size: 29px; color: var(--ink); }
  .person-name { top: 130px; font-size: 22px; color: var(--gold); }
  .person-role { top: 152px; font-size: 16px; color: var(--ink-soft); }
  .contact { font-size: 14px; color: var(--ink-soft); }
  .contact--street { top: 192px; }
  .contact--city { top: 211px; }
  .contact--phone { top: 240px; }
  .contact--email { top: 260px; }
  .contact--web { top: 279px; }
  .motto-script {
    top: 306px;
    left: -4px !important;
    font-family: "Alex Brush", cursive;
    font-size: 30px;
    color: var(--gold);
  }

  .portrait {
    position: absolute;
    left: 31px; top: 26px;
    width: 142px; height: 142px;
    border-radius: 50%;
    background: radial-gradient(circle at 50% 45%, #d9c7b2, #a08c7a 60%, #6e645c);
  }
  .back-footer {
    position: absolute;
    left: 0; right: 0; top: 292px;
    text-align: center;
  }
  .motto-back {
    font-style: italic;
    font-weight: 700;
    font-size: 31px;
    line-height: 1.1;
    color: var(--ink);
  }
  .web-back {
    font-size: 23px;
    line-height: 1.2;
    color: var(--ink);
  }
</style>
</head>
<body>
  <section class="card card--front">
    <svg class="front-photo" viewBox="0 0 686 392" aria-hidden="false">
      <defs>
        <linearGradient id="photoTone" x1="0" y1="0" x2="1" y2="1">
          <stop offset="0" stop-color="var(--photo-light)"/>
          <stop offset="0.55" stop-color="var(--photo-mid)"/>
          <stop offset="1" stop-color="var(--photo-dark)"/>
        </linearGradient>
      </defs>
      <path d="M235,0 C300,10 330,110 362,205 C392,295 425,362 478,392 L686,392 L686,0 Z"
            fill="rgba(0,0,0,0.18)" transform="translate(-4,0)"/>
      <path role="img" aria-label="Photo of a woman receiving a facial with a cream mask, hands at her temples, towels and a candle beside her"
            d="M235,0 C300,10 330,110 362,205 C392,295 425,362 478,392 L686,392 L686,0 Z"
            fill="url(#photoTone)"/>
    </svg>
    <div class="front-text">
      <p class="business-name">Coastline Skin Care</p>
      <p class="person-name">Lorena Bistrica Vondel</p>
      <p class="person-role">Esthetician</p>
      <p class="contact contact--street">7183 SW 9th Avenue</p>
      <p class="contact contact--city">Dallow WA 98321</p>
      <p class="contact contact--phone">312.485.1937</p>
      <p class="contact contact--email">marlowskincare@examplemail.com</p>
      <p class="contact contact--web">www.marlowskincare.example</p>
      <p class="motto-script">Helping you find beautiful!</p>
    </div>
  </section>

  <section class="card card--back">
    <div class="portrait" role="img" aria-label="Portrait photo of the esthetician in a white uniform"></div>
    <div class="back-footer">
      <p class="motto-back">Helping you find beautiful</p>
      <p class="web-back">www.marlowskincare.example</p>
    </div>
  </section>
</body>
</html>
```